Custom Woodworking and Rock Design

We specialize in original, high quality, wood and rock art. It’s should be self explanatory ask questions if you need. Your team designing a logo. Furniture is custom made to order. Rocks are designed depending on consumer needs. Wood and rock can also be combined for custom work. Painted rocks on vintage wood. Custom chairs and cabinets. Artistic rocks for multiple uses:garden, magnets, custom. All ideas and requests are welcome.

Target Market(s)

All

Contact Information for Business Card

Mara Dolby
Talverstonecraft@mailvoro.net

Font styles to use
Sans Serif

Requirements
Must have
• Clear lettering
Nice to have
• Eye catching
Should not have
• Blurr

```html
<!DOCTYPE html>
<html lang="en">
<head>
<meta charset="utf-8">
<title>The Pebble Perch – Business Card</title>
<link href="https://fonts.googleapis.com/css2?family=Lato:wght@400;700&display=swap" rel="stylesheet">
<style>
  :root {
    --backdrop: #2b2b2b;
    --card: #ffffff;
    --ink: #6f6f6f;
    --ink-dark: #5a5a5a;
    --arc: #e3e3e3;
    --arc-deep: #d2d2d2;
    --accent: #4aa3df;
    --pattern-a: #f7f7f7;
    --pattern-b: #ececec;
  }
  * { box-sizing: border-box; margin: 0; padding: 0; }
  html, body {
    width: 1200px; height: 770px; overflow: hidden;
    background: var(--backdrop);
    font-family: "Lato", sans-serif;
  }
  .stage {
    width: 1200px; height: 770px;
    display: flex; align-items: center; justify-content: center; gap: 50px;
  }
  .card {
    position: relative;
    width: 525px; height: 300px;
    background: var(--card);
    border-radius: 18px;
    overflow: hidden;
  }
  /* front */
  .card-front .pebble-pattern {
    position: absolute; inset: 0;
    background: radial-gradient(ellipse at center, var(--pattern-a) 0%, var(--pattern-b) 100%);
  }
  .brand {
    position: absolute;
    display: flex; flex-direction: column; align-items: center; gap: 10px;
    color: var(--ink);
    font-weight: 700; font-size: 15px; letter-spacing: 0.5px;
  }
  .brand-dot {
    width: 62px; height: 62px; border-radius: 50%;
    border: 2px solid var(--ink);
  }
  .card-front .brand { left: 50%; top: 50%; transform: translate(-50%, -50%); }
  /* back */
  .arcs { position: absolute; inset: 0; }
  .card-back .brand { right: 42px; top: 30px; }
  .holder { position: absolute; left: 40px; top: 112px; color: var(--ink); }
  .holder-name { font-size: 22px; font-weight: 700; letter-spacing: 1px; }
  .holder-role { font-size: 13px; font-weight: 700; margin-top: 2px; color: var(--ink-dark); }
  .contacts {
    position: absolute; left: 40px; top: 186px;
    list-style: none; color: var(--ink); font-size: 16px; line-height: 20px;
  }
  .contacts li { display: flex; align-items: center; gap: 8px; }
  .contacts svg { width: 13px; height: 13px; flex: none; }
</style>
</head>
<body>
<main class="stage">
  <section class="card card-front">
    <div class="pebble-pattern" role="img" aria-label="Scattered hand-drawn light grey pebble outlines across the card"></div>
    <div class="brand">
      <span class="brand-dot"></span>
      <span class="brand-name">The Pebble Perch</span>
    </div>
  </section>

  <section class="card card-back">
    <svg class="arcs" viewBox="0 0 525 300" aria-hidden="true">
      <circle cx="470" cy="20" r="250" fill="none" stroke="var(--arc)" stroke-width="26"/>
      <circle cx="300" cy="60" r="250" fill="none" stroke="var(--arc-deep)" stroke-width="26" opacity="0.7"/>
    </svg>
    <div class="brand">
      <span class="brand-dot"></span>
      <span class="brand-name">The Pebble Perch</span>
    </div>
    <div class="holder">
      <p class="holder-name">Mara Dolby</p>
      <p class="holder-role">Director/Owner</p>
    </div>
    <ul class="contacts">
      <li><svg viewBox="0 0 14 14"><circle cx="7" cy="7" r="7" fill="var(--accent)"/><rect x="5" y="3.5" width="4" height="7" rx="1" fill="#fff"/></svg>123 456 7890</li>
      <li><svg viewBox="0 0 14 14"><circle cx="7" cy="7" r="7" fill="var(--accent)"/><circle cx="7" cy="7" r="3.5" fill="none" stroke="#fff" stroke-width="1"/><path d="M3.5 7h7M7 3.5v7" stroke="#fff" stroke-width="1"/></svg>talverstonecraft.net</li>
      <li><svg viewBox="0 0 14 14"><circle cx="7" cy="7" r="7" fill="var(--accent)"/><rect x="3.5" y="4.5" width="7" height="5" fill="#fff"/><path d="M3.5 4.5l3.5 3 3.5-3" fill="none" stroke="var(--accent)" stroke-width="0.8"/></svg>Talverstonecraft@mailvoro.net</li>
      <li><svg viewBox="0 0 14 14"><circle cx="7" cy="7" r="7" fill="var(--accent)"/><rect x="4" y="6" width="6" height="4" fill="#fff"/><rect x="5" y="3.5" width="4" height="2.5" fill="#fff"/></svg>444 555 6667</li>
    </ul>
  </section>
</main>
</body>
</html>
```